5 Planner Covers for Teacher Planners

Hello,
I currently run a Speech-Language Pathologist website and have created a planner for my fellow Speech Therapist. I would like someone to create 5 different planner covers so my followers will have different options to choose from.
Here is my planner from last year to give you an idea of what the planner will look like http://www.talkwellnook.example/free-slp-planner/
My followers are mostly women aged 25-50. However, I don't want the covers to be overly girly or excessive with flowers. Simple is better.
I'd also like there to be an editable text box to allow the Speech Therapist to type their name on their cover if they wish.
Planner Cover can say any of the following: SLP Planner, Planner, Speech Therapy Planner, Speech-Language Pathologist (maybe this title could be editable as well??).
To give you an idea I have uploaded a screenshot of last year's planners cover that I made myself.
What I am looking for:
-Size 8.5" by 11"
-5 different planner covers
-1 gender-neutral cover
-simple design
-limited flowers (or overly girly
-text box to add a personal name
-Possible titles: SLP Planner, Planner, Speech Therapy Planner, Speech-Language Pathologist (maybe this title could be editable as well??)
Target Market(s)
Women aged 25-50
Colors
Designer to choose colors to be used in the design.
Requirements
Must have
- What I am looking for:
-Size 8.5" by 11"
-1 gender-neutral cover
-simple design
Nice to have
- I've uploaded some that I like from Craftly to give you an idea.
Here is my craftly store https://www.craftly.example/shop/QuietMeadowHome to give you an idea of things I like.
I like Marla Hensley and her simple elegant rustic style.

```html
<!DOCTYPE html>
<html lang="en">
<head>
<meta charset="utf-8">
<title>Planner Cover</title>
<link rel="stylesheet" href="https://fonts.googleapis.com/css2?family=Parisienne&display=swap">
<style>
  :root {
    --sun-yellow: #fbd63a;
    --warm-orange: #f5a23a;
    --deep-orange: #f07a34;
    --coral-red: #e8423d;
    --blush-pink: #ea8cab;
    --soft-lavender: #e7c3df;
    --cream-glow: #fdf6ef;
    --label-white: #ffffff;
  }
  * { margin: 0; padding: 0; box-sizing: border-box; }
  html, body {
    width: 926px;
    height: 1200px;
    overflow: hidden;
    background: var(--warm-orange);
  }
  .planner-cover {
    position: relative;
    width: 926px;
    height: 1200px;
    overflow: hidden;
    background:
      radial-gradient(ellipse 460px 520px at 30% 18%, var(--sun-yellow) 0%, rgba(251,214,58,0.85) 45%, rgba(251,214,58,0) 100%),
      radial-gradient(ellipse 420px 480px at 98% 46%, var(--cream-glow) 0%, rgba(253,246,239,0.8) 35%, rgba(253,246,239,0) 100%),
      radial-gradient(ellipse 380px 420px at 100% 98%, var(--soft-lavender) 0%, rgba(231,195,223,0.7) 50%, rgba(231,195,223,0) 100%),
      radial-gradient(ellipse 380px 360px at 62% 92%, var(--blush-pink) 0%, rgba(234,140,171,0.6) 45%, rgba(234,140,171,0) 100%),
      radial-gradient(ellipse 460px 520px at 4% 92%, var(--coral-red) 0%, rgba(232,66,61,0.9) 45%, rgba(232,66,61,0) 100%),
      radial-gradient(ellipse 420px 420px at 20% 62%, var(--deep-orange) 0%, rgba(240,122,52,0) 100%),
      linear-gradient(160deg, var(--sun-yellow) 0%, var(--warm-orange) 45%, var(--deep-orange) 100%);
  }
  .name-label {
    position: absolute;
    left: 0;
    top: 0;
    width: 926px;
    height: 1200px;
  }
  .name-label .frame-outer {
    fill: none;
    stroke: var(--label-white);
    stroke-width: 7;
  }
  .name-label .frame-inner {
    fill: none;
    stroke: var(--label-white);
    stroke-width: 3;
  }
  .name-label .name-line {
    stroke: var(--label-white);
    stroke-width: 2;
  }
  .label-title {
    position: absolute;
    left: 0;
    width: 926px;
    text-align: center;
    color: var(--label-white);
    font-family: "Parisienne", cursive;
  }
  .label-title.planner-word {
    top: 500px;
    font-size: 52px;
    line-height: 1;
  }
  .label-title.belongs-to {
    top: 567px;
    font-size: 27px;
    line-height: 1;
  }
</style>
</head>
<body>
  <main class="planner-cover">
    <svg class="name-label" viewBox="0 0 926 1200" aria-hidden="true">
      <path class="frame-outer" d="M 300 520 C 360 452, 564 452, 624 520 Q 662 522 666 552 L 666 646 Q 662 678 624 680 C 564 748, 360 748, 300 680 Q 262 678 258 646 L 258 552 Q 262 522 300 520 Z"/>
      <path class="frame-inner" d="M 306 534 C 366 470, 558 470, 618 534 Q 650 536 653 560 L 653 638 Q 650 664 618 666 C 558 730, 366 730, 306 666 Q 274 664 271 638 L 271 560 Q 274 536 306 534 Z"/>
      <line class="name-line" x1="345" y1="664" x2="580" y2="664"/>
    </svg>
    <h1 class="label-title planner-word">Planner</h1>
    <p class="label-title belongs-to">belongs to</p>
  </main>
</body>
</html>
```